Soy Candle Labels

We sell soy candles in recycled wine bottles. The wine bottle is cut in half and filled with pure and natural soy wax and scented with essential oils.
Our product represents good use of up cycling materials for a better use. The product is all natural and eco friendly.
You can see good use of labels and branding for a company in America that does the same thing http://marrowlanewicks.example/
Trya dn keep the label uncomplicated like the above labels.
We will need an area to hand stamp the scent. Similar to the labels used on the above website.
We would prefer to use a white or off white paper label with gold or bronze printing - limit the use of colour and keep the label simple and sophisticated.
Brambrel Candle Co. is our company name. Brambrel being the predominant name and candle co. written small underneath right justified.
Die cut labels might look better than a rectangle.
Dimensions should be 90mm Wide x 90mm High
The final design should communicate a professional and quality product. But stay modern and professional. Clean, elegant and sophisticated.
Can use wording such as: Hand Poured, Premium Soy Wax, All Natural, Up cycled
Have a look at the attached image for the look and feel we are going for.
Updates
Designers are having a little bit of trouble interpreting the brief into a viable design. To assist perhaps you can look at WINE LABELS on google images. Design your label around an existing style wine label to give the canld ethe feel of being a bottle of wine. Get creative! :)
Reason: We require more designs. We havnt quite got what were looking for.
Please see brief.

```html
<!DOCTYPE html>
<html lang="en">
<head>
<meta charset="utf-8">
<title>Brambrel Candle Co. – Soy Candle Label</title>
<link rel="stylesheet" href="https://fonts.googleapis.com/css2?family=Marcellus+SC&family=Staatliches&display=swap">
<style>
  :root {
    --paper: #fefbe3;
    --bronze: #b8692a;
    --bronze-soft: #dba77d;
    --ornament-tone: #f5e2c6;
    --stamp-green: #b5c68f;
  }
  * { margin: 0; padding: 0; box-sizing: border-box; }
  html, body {
    width: 1200px;
    height: 1200px;
    overflow: hidden;
    background: var(--paper);
  }
  .label {
    position: relative;
    width: 1200px;
    height: 1200px;
    background: var(--paper);
    color: var(--bronze);
    font-family: "Marcellus SC", serif;
  }
  .top-band {
    position: absolute;
    left: 0; top: 0;
    width: 1200px; height: 15px;
    background: var(--bronze);
  }
  .ornament-border {
    position: absolute;
    left: 0; top: 58px;
    width: 1200px; height: 246px;
    background: linear-gradient(180deg, var(--paper) 0%, var(--ornament-tone) 50%, var(--paper) 100%);
  }
  .claims {
    position: absolute;
    left: 70px; top: 384px;
    font-size: 30px;
    letter-spacing: 0.5px;
    white-space: nowrap;
  }
  .claims .divider { margin: 0 14px; }
  .double-rule {
    position: absolute;
    left: 0; top: 447px;
    width: 691px; height: 10px;
    border-top: 2px solid var(--bronze);
    border-bottom: 2px solid var(--bronze);
  }
  .scent-caption {
    position: absolute;
    left: 832px; top: 466px;
    transform: translate(-50%, -50%) rotate(-90deg);
    font-size: 25px;
    letter-spacing: 1px;
  }
  .scent-stamp {
    position: absolute;
    left: 863px; top: 320px;
    width: 294px; height: 294px;
    border: 3px solid var(--bronze-soft);
    border-radius: 50%;
    display: flex;
    align-items: center;
    justify-content: center;
    text-align: center;
    font-family: "Staatliches", sans-serif;
    font-size: 70px;
    line-height: 0.92;
    color: var(--stamp-green);
  }
  .brand-name {
    position: absolute;
    left: 0; right: 0; top: 730px;
    text-align: center;
    font-size: 205px;
    line-height: 1;
    color: var(--bronze);
    white-space: nowrap;
  }
  .brand-sub {
    position: absolute;
    right: 57px; top: 980px;
    font-size: 44px;
    letter-spacing: 1px;
  }
  .origin, .net-weight {
    position: absolute;
    top: 1120px;
    font-size: 27px;
    letter-spacing: 0.3px;
    white-space: nowrap;
  }
  .origin { left: 66px; }
  .net-weight { right: 70px; }
</style>
</head>
<body>
  <main class="label">
    <div class="top-band"></div>

    <div class="ornament-border" role="img" aria-label="Row of five outlined lotus-flower ornaments in soft bronze"></div>

    <p class="claims">Hand Poured<span class="divider">|</span>All Natural Soy</p>
    <div class="double-rule"></div>

    <p class="scent-caption">Scent</p>
    <div class="scent-stamp"><span>Scent<br>Name</span></div>

    <h1 class="brand-name">Brambrel</h1>
    <p class="brand-sub">Candle Co.</p>

    <p class="origin">Product of Australia</p>
    <p class="net-weight">320 gm. Premium Soy Wax</p>
  </main>
</body>
</html>
```